Banner Ad Design Set

We need a set of web and social banner ads to support an upcoming campaign. Campaign concept and logo are attached.

Once approved, we will require the original photoshop design files.

All text should be editable in case of any tweaks down the line required.

250 x 250 – Square
468 x 60 – Banner
728 x 90 – Leaderboard
300 x 250 – Inline Rectangle
336 x 280 – Large Rectangle
120 x 600 – Skyscraper
160 x 600 – Wide Skyscraper
300 x 600 – Half-Page Ad
970 x 90 – Large Leaderboard

Social:
1200x628 - Quorvale
440x220 - Zindlet
1080x1080 - Maplorixa

```html
<!DOCTYPE html>
<html lang="en">
<head>
<meta charset="utf-8">
<title>Built for the unexpected – Banner Ad Set</title>
<link rel="stylesheet" href="https://fonts.googleapis.com/css2?family=Open+Sans:ital,wght@0,600;0,700;1,400;1,700&family=Cousine&display=swap">
<style>
  :root {
    --navy: #070c3a;
    --deep-blue: #0b2a8c;
    --blue: #1a5fd6;
    --cyan: #3fd9d0;
    --white: #ffffff;
    --orange: #ff8200;
    --orange-text: #ff8a1a;
    --tagline: #0a0f2e;
    --canvas: #ffffff;
  }
  * { box-sizing: border-box; margin: 0; padding: 0; }
  html, body { width: 1200px; height: 781px; overflow: hidden; background: var(--canvas); }
  .canvas { position: relative; width: 1200px; height: 781px; overflow: hidden; }

  .banner { position: absolute; overflow: hidden; font-family: "Open Sans", sans-serif; }
  .banner__art {
    position: absolute; inset: 0;
    background:
      radial-gradient(ellipse at 85% 90%, rgba(63,217,208,0.75) 0%, rgba(63,217,208,0) 45%),
      linear-gradient(115deg, var(--navy) 0%, var(--deep-blue) 45%, var(--blue) 100%);
  }
  .banner--strip .banner__art {
    background:
      radial-gradient(ellipse at 95% 60%, rgba(63,217,208,0.55) 0%, rgba(63,217,208,0) 30%),
      linear-gradient(90deg, var(--navy) 0%, var(--deep-blue) 45%, var(--blue) 100%);
  }
  .banner--tall .banner__art {
    background:
      radial-gradient(ellipse at 50% 95%, rgba(63,217,208,0.7) 0%, rgba(63,217,208,0) 40%),
      linear-gradient(180deg, var(--navy) 0%, var(--deep-blue) 45%, var(--blue) 100%);
  }

  .headline { position: absolute; color: var(--white); font-weight: 600; line-height: 0.93; letter-spacing: -0.01em; white-space: nowrap; }
  .body-copy { position: absolute; color: var(--orange-text); font-style: italic; font-weight: 400; line-height: 1.4; white-space: nowrap; }
  .body-copy--bold { font-weight: 700; }
  .cta { position: absolute; background: var(--orange); color: var(--white); font-family: "Cousine", monospace; display: flex; align-items: center; justify-content: center; white-space: nowrap; }
  .tagline { position: absolute; font-family: "Cousine", monospace; color: var(--tagline); white-space: nowrap; }

  /* Skyscraper 120x600 */
  .skyscraper { left: 43px; top: 35px; width: 120px; height: 600px; }
  .skyscraper .headline { left: 0; width: 120px; top: 64px; font-size: 19px; text-align: center; line-height: 1.3; }
  .skyscraper .body-copy { left: 0; width: 120px; top: 202px; font-size: 11px; text-align: center; line-height: 1.38; }
  .skyscraper .cta { left: 2px; top: 466px; width: 113px; height: 17px; font-size: 10px; }

  /* Large leaderboard 970x90 */
  .leaderboard-lg { left: 193px; top: 40px; width: 970px; height: 90px; }
  .leaderboard-lg .headline { left: 32px; top: 8px; font-size: 37.5px; }
  .leaderboard-lg .body-copy { left: 313px; top: 15px; font-size: 15.2px; line-height: 1.25; }
  .leaderboard-lg .tagline { left: 724px; top: 31px; font-size: 25px; }

  /* Leaderboard 728x90 */
  .leaderboard { left: 193px; top: 146px; width: 727px; height: 90px; }
  .leaderboard .headline { left: 8px; top: 10px; font-size: 37.5px; }
  .leaderboard .body-copy { left: 254px; top: 14px; font-size: 14.3px; line-height: 1.35; }
  .leaderboard .tagline { left: 577px; top: 34px; font-size: 16.5px; }

  /* Social 440x220 */
  .social-wide { left: 191px; top: 247px; width: 518px; height: 271px; }
  .social-wide .headline { left: 28px; top: 32px; font-size: 37px; line-height: 0.9; }
  .social-wide .body-copy { left: 30px; top: 118px; font-size: 13px; line-height: 1.45; }
  .social-wide .cta { left: 30px; top: 195px; width: 160px; height: 25px; font-size: 14px; }
  .social-wide .tagline { left: 396px; top: 238px; font-size: 11px; }

  /* Square 467 */
  .square { left: 731px; top: 246px; width: 467px; height: 467px; }
  .square .headline { left: 80px; top: 44px; font-size: 54px; }
  .square .body-copy { left: 35px; top: 172px; font-size: 18.5px; line-height: 1.3; }
  .square .cta { left: 117px; top: 323px; width: 232px; height: 35px; font-size: 18px; }
  .square .tagline { left: 150px; top: 426px; font-size: 20px; }

  /* Small banner */
  .mini { left: 193px; top: 534px; width: 190px; height: 95px; }
  .mini .headline { left: 9px; top: 11px; font-size: 13.5px; }
  .mini .body-copy { left: 10px; top: 42px; font-size: 5px; }
  .mini .cta { left: 10px; top: 71px; width: 60px; height: 9px; font-size: 5px; }
  .mini .tagline { right: 6px; top: 86px; font-size: 4.7px; }

  /* Inline rectangle 320x250 */
  .rectangle { left: 396px; top: 533px; width: 320px; height: 250px; }
  .rectangle .headline { left: 38px; top: 15px; font-size: 42px; }
  .rectangle .body-copy { left: 37px; top: 112px; font-size: 10.5px; line-height: 1.4; }
  .rectangle .cta { left: 68px; top: 191px; width: 184px; height: 28px; font-size: 15px; }
  .rectangle .tagline { left: 199px; top: 229px; font-size: 11px; }
</style>
</head>
<body>
<main class="canvas">

  <section class="banner banner--tall skyscraper">
    <div class="banner__art" role="img" aria-label="Dark blue gradient backdrop with glowing DNA helix and hexagon network"></div>
    <h2 class="headline">Built for the<br>unexpected.</h2>
    <p class="body-copy body-copy--bold">see how automa-<br>tion-enabled<br>backup solutions<br>are giving IT pros<br>37% more time<br>in their day<br>and 100% recov-<br>ery confidence<br>in the inevitable.</p>
    <span class="cta">try it free &gt;</span>
  </section>

  <section class="banner banner--strip leaderboard-lg">
    <div class="banner__art" role="img" aria-label="Dark blue gradient backdrop with glowing DNA helix and hexagon network"></div>
    <h2 class="headline">Built for the<br>unexpected.</h2>
    <p class="body-copy">see how automation-enabled backup solutions<br>are giving IT pros 37% more time in their day<br>and 100% recovery confidence in the inevitable.</p>
    <span class="tagline">ITs IN OUR DNA</span>
  </section>

  <section class="banner banner--strip leaderboard">
    <div class="banner__art" role="img" aria-label="Dark blue gradient backdrop with glowing DNA helix and hexagon network"></div>
    <h2 class="headline">Built for the<br>unexpected.</h2>
    <p class="body-copy">see how automation-enabled backup solutions<br>are giving IT pros 37% more time in their day<br>and 100% recovery confidence in the inevitable.</p>
    <span class="tagline">ITs IN OUR DNA</span>
  </section>

  <section class="banner social-wide">
    <div class="banner__art" role="img" aria-label="Dark blue gradient backdrop with glowing DNA helix and hexagon network"></div>
    <h2 class="headline">Built for the<br>unexpected.</h2>
    <p class="body-copy">see how automation-enabled backup solutions<br>are giving IT pros 37% more time in their day<br>and 100% recovery confidence in the inevitable.</p>
    <span class="cta">try it free &gt;</span>
    <span class="tagline">ITs IN OUR DNA</span>
  </section>

  <section class="banner square">
    <div class="banner__art" role="img" aria-label="Dark blue gradient backdrop with glowing DNA helix and hexagon network"></div>
    <h2 class="headline">Built for the<br>unexpected.</h2>
    <p class="body-copy">see how automation-enabled backup solutions<br>are giving IT pros 37% more time in their day<br>and 100% recovery confidence in the inevitable.</p>
    <span class="cta">try it free &gt;</span>
    <span class="tagline">ITs IN OUR DNA</span>
  </section>

  <section class="banner mini">
    <div class="banner__art" role="img" aria-label="Dark blue gradient backdrop with glowing DNA helix and hexagon network"></div>
    <h2 class="headline">Built for the<br>unexpected.</h2>
    <p class="body-copy">see how automation-enabled backup solutions<br>are giving IT pros 37% more time in their day<br>and 100% recovery confidence in the inevitable.</p>
    <span class="cta">try it free &gt;</span>
    <span class="tagline">ITs IN OUR DNA</span>
  </section>

  <section class="banner rectangle">
    <div class="banner__art" role="img" aria-label="Dark blue gradient backdrop with glowing DNA helix and hexagon network"></div>
    <h2 class="headline">Built for the<br>unexpected.</h2>
    <p class="body-copy body-copy--bold">see how automation-enabled backup solutions<br>are giving IT pros 37% more time in their day<br>and 100% recovery confidence in the inevitable.</p>
    <span class="cta">try it free &gt;</span>
    <span class="tagline">ITs IN OUR DNA</span>
  </section>

</main>
</body>
</html>
```